Harrowfield Security Solutions Trade Show

Backdrop for trade show and table cover. Colors to use are red, black and silver/grey . Logo attached. If you are able to view the website and pull any images, that would be great. Website is https://harrowfieldsecuritywx.com/

```html
<!DOCTYPE html>
<html lang="en">
<head>
<meta charset="utf-8">
<title>Harrowfield Security Solutions – Trade Show Backdrop &amp; Table Cover</title>
<link rel="stylesheet" href="https://fonts.googleapis.com/css2?family=League+Gothic&family=Poppins:wght@600&display=swap">
<style>
  :root {
    --red: #e5421d;
    --red-deep: #d33417;
    --ink: #3a3a3a;
    --black: #0e0e0e;
    --charcoal: #4a4a4a;
    --silver: #ececec;
    --silver-edge: #d6d6d6;
    --stage: #c8c8c8;
    --white: #ffffff;
  }
  * { margin: 0; padding: 0; box-sizing: border-box; }
  html, body { width: 1200px; height: 840px; overflow: hidden; }
  body { background: var(--stage); position: relative; font-family: "League Gothic", "Arial Narrow", sans-serif; }

  /* ---------- Table cover ---------- */
  .table-cover {
    position: absolute; left: 40px; top: 410px; width: 320px; height: 380px;
    display: flex; flex-direction: column;
  }
  .table-cover__cap { height: 34px; background: var(--black); border-radius: 8px 8px 0 0; }
  .table-cover__body {
    position: relative; flex: 1;
    background: radial-gradient(ellipse at 50% 40%, #f7f7f7 0%, var(--silver) 60%, var(--silver-edge) 100%);
    overflow: hidden;
  }
  .table-cover__brand {
    position: absolute; top: 30px; left: 0; right: 0;
    display: flex; flex-direction: column; align-items: center; color: var(--red);
  }
  .table-cover__mark { width: 64px; height: 64px; border-radius: 50%; background: var(--red); margin-bottom: 12px; }
  .table-cover__name { font-size: 50px; line-height: 0.95; letter-spacing: 2px; }
  .table-cover__tag { font-size: 24px; line-height: 1; letter-spacing: 5px; }
  .table-cover__waves { position: absolute; left: 0; bottom: 0; width: 100%; height: 120px; }
  .table-cover__url {
    position: absolute; left: 14px; bottom: 30px;
    font-family: "Poppins", sans-serif; font-weight: 600; font-size: 11px; color: var(--white);
  }
  .table-cover__base { height: 56px; background: var(--black); border-radius: 0 0 10px 10px; border-top: 4px solid #222; }

  /* ---------- Backdrop ---------- */
  .backdrop {
    position: absolute; left: 390px; top: 50px; width: 770px; height: 740px;
    background: radial-gradient(ellipse at 35% 40%, #fafafa 0%, var(--silver) 55%, var(--silver-edge) 100%);
    overflow: hidden;
  }
  .backdrop__art { position: absolute; inset: 0; width: 100%; height: 100%; }

  .brand { position: absolute; left: 28px; top: 36px; display: flex; align-items: center; gap: 26px; color: var(--red); }
  .brand__mark { width: 150px; height: 150px; border-radius: 50%; background: var(--red); flex: none; }
  .brand__name { font-size: 112px; line-height: 0.9; letter-spacing: 4px; }
  .brand__tag { font-size: 52px; line-height: 1; letter-spacing: 9px; }

  .headline {
    position: absolute; left: 22px; top: 262px;
    font-size: 64px; line-height: 0.92; color: var(--ink); text-transform: uppercase;
  }
  .headline em { font-style: normal; color: var(--red); }
  .headline__rule { display: block; width: 48px; height: 4px; background: var(--red); margin-top: 8px; }

  .features {
    position: absolute; left: 20px; top: 400px; width: 370px;
    display: grid; grid-template-columns: repeat(3, 1fr); grid-template-rows: 74px 74px;
  }
  .feature {
    display: flex; flex-direction: column; align-items: center; justify-content: center; gap: 6px;
    font-size: 16px; color: var(--ink); text-transform: uppercase; letter-spacing: 0.3px;
    border-right: 1px dotted #e69a88;
  }
  .feature:nth-child(3n) { border-right: none; }
  .feature:nth-child(-n+3) { border-bottom: 1px dotted #e69a88; }
  .feature svg { width: 28px; height: 28px; fill: none; stroke: var(--red); stroke-width: 1.6; stroke-linecap: round; stroke-linejoin: round; }

  .backdrop__url {
    position: absolute; left: 30px; top: 640px;
    font-family: "Poppins", sans-serif; font-weight: 600; font-size: 15px; color: var(--silver);
  }
  .url-tld { color: var(--red); }
</style>
</head>
<body>

  <!-- Table cover -->
  <section class="table-cover" aria-label="Table cover">
    <div class="table-cover__cap"></div>
    <div class="table-cover__body">
      <div class="table-cover__brand">
        <span class="table-cover__mark"></span>
        <span class="table-cover__name">HARROWFIELD</span>
        <span class="table-cover__tag">SECURITY SOLUTIONS</span>
      </div>
      <svg class="table-cover__waves" viewBox="0 0 320 120" preserveAspectRatio="none">
        <path d="M0 20 C70 0 130 10 190 40 C240 62 280 70 320 62 L320 60 C270 58 230 40 180 22 C120 2 60 4 0 14 Z" fill="var(--red)"/>
        <path d="M0 38 C80 18 150 30 210 58 C250 74 290 78 320 72 L320 120 L0 120 Z" fill="var(--black)"/>
        <path d="M0 34 C80 14 150 26 210 54 C250 70 290 74 320 68 L320 72 C290 78 250 74 210 58 C150 30 80 18 0 38 Z" fill="var(--white)"/>
      </svg>
      <p class="table-cover__url">HarrowfieldSecuritywx<span class="url-tld">.com</span></p>
    </div>
    <div class="table-cover__base"></div>
  </section>

  <!-- Backdrop -->
  <section class="backdrop" aria-label="Backdrop">
    <svg class="backdrop__art" viewBox="0 0 770 740" preserveAspectRatio="none">
      <defs>
        <linearGradient id="photo-tone" x1="0" y1="0" x2="1" y2="1">
          <stop offset="0" stop-color="#b9b0a8"/>
          <stop offset="0.45" stop-color="#8c8fa6"/>
          <stop offset="1" stop-color="#2c3e78"/>
        </linearGradient>
        <linearGradient id="band-tone" x1="0" y1="0" x2="1" y2="0">
          <stop offset="0" stop-color="#0d0d0d"/>
          <stop offset="1" stop-color="#4d4d4d"/>
        </linearGradient>
      </defs>

      <!-- bottom band -->
      <path d="M0 565 C90 540 190 548 280 580 C380 616 470 640 520 650 L560 660 C540 660 430 640 330 612 C220 580 110 566 0 582 Z" fill="var(--red)"/>
      <path d="M0 600 C110 570 220 580 320 620 C420 660 510 700 610 740 L0 740 Z" fill="url(#band-tone)"/>
      <path d="M0 592 C110 562 220 572 320 612 C420 652 510 692 610 732 L610 740 C510 700 420 660 320 620 C220 580 110 570 0 600 Z" fill="var(--white)"/>
      <path d="M260 602 C340 630 420 660 500 668 C540 672 570 672 600 668 L600 680 C560 690 500 690 430 672 C370 656 310 630 260 602 Z" fill="var(--red)"/>

      <!-- shield frame -->
      <path d="M430 308 L660 204 L770 252 L770 740 L565 740 C478 620 430 460 430 308 Z" fill="var(--red)"/>
      <path d="M446 326 L660 230 L770 277 L770 740 L582 740 C496 622 446 470 446 326 Z" fill="var(--white)"/>
      <path role="img" aria-label="Photo: security guard in cap and navy jacket speaking into a handheld radio, blurred indoor venue behind"
            d="M462 344 L660 254 L770 300 L770 740 L598 740 C512 624 462 480 462 344 Z" fill="url(#photo-tone)"/>
    </svg>

    <header class="brand">
      <span class="brand__mark"></span>
      <div>
        <div class="brand__name">HARROWFIELD</div>
        <div class="brand__tag">SECURITY SOLUTIONS</div>
      </div>
    </header>

    <h1 class="headline">
      Exceptional <em>Security</em><br>
      <em>Guard</em> Solutions
      <span class="headline__rule"></span>
    </h1>

    <ul class="features" role="list">
      <li class="feature">
        <svg viewBox="0 0 28 28"><path d="M6 3 H14 V25 H6 Z"/><path d="M14 5 L19 7 V23 L14 25"/><path d="M18 14 H26 M23 11 L26 14 L23 17"/></svg>
        Expertise &amp; Experience
      </li>
      <li class="feature">
        <svg viewBox="0 0 28 28"><circle cx="14" cy="16" r="10"/><path d="M12 3 H16 M14 3 V6 M14 16 L18 13 M14 16 V10"/></svg>
        24/7 Availability
      </li>
      <li class="feature">
        <svg viewBox="0 0 28 28"><circle cx="14" cy="10" r="5"/><path d="M5 26 C5 19 9 16 14 16 C19 16 23 19 23 26 Z"/><path d="M7 8 H21"/></svg>
        Highly Trained
      </li>
      <li class="feature">
        <svg viewBox="0 0 28 28"><path d="M2 16 H9 V6 H14 V22 H19 V14 H26"/></svg>
        Security Solutions
      </li>
      <li class="feature">
        <svg viewBox="0 0 28 28"><path d="M14 7 L21 10 V18 L14 21 L7 18 V10 Z M7 10 L14 13 L21 10 M14 13 V21"/><path d="M4 14 A10 10 0 0 1 20 5 M24 14 A10 10 0 0 1 8 23"/></svg>
        Rapid Response Times
      </li>
      <li class="feature">
        <svg viewBox="0 0 28 28"><circle cx="14" cy="14" r="11"/><circle cx="14" cy="14" r="5"/><circle cx="14" cy="14" r="1.5"/><path d="M14 14 L21 7"/></svg>
        Proven Track Record
      </li>
    </ul>

    <p class="backdrop__url">HarrowfieldSecuritywx<span class="url-tld">.com</span></p>
  </section>

</body>
</html>
```